HWN Structures Ltd- building and maintenance company looking to create professional branding for m

creation of a website for a building and maintenance company,
will need a gallery and references/ reviews page
homepage to have some company information with rolling photos of completed works
all suggestions welcome on additional requirements for website.
layout should be easy to navigate.

Target Market(s)

30-70s homeowners with mid to high income

Logo Text

HWN Structures Ltd

Coding

Coded - Design and coding required

Number of Pages Required

4 page

```html
<!DOCTYPE html>
<html lang="en">
<head>
<meta charset="utf-8">
<title>HWN Structures Ltd</title>
<link href="https://fonts.googleapis.com/css2?family=Lato:ital,wght@0,300;0,400;0,700;0,900;1,400&display=swap" rel="stylesheet">
<style>
:root{
  --blue:#0b3d9c;
  --blue-link:#1450b4;
  --ink:#333;
  --body:#3c3c3c;
  --topbar:#2e2e2e;
  --footer:#1f1f1f;
  --footer-text:#b9b9b9;
  --panel:#efefef;
  --white:#fff;
}
*{margin:0;padding:0;box-sizing:border-box}
html,body{width:1200px;height:3364px;overflow:hidden}
body{font-family:"Lato",sans-serif;color:var(--body);background:var(--white);position:relative}
section,header,footer{position:absolute;left:0;width:1200px}
.title{font-weight:300;font-size:50px;color:var(--ink);text-align:center;line-height:1.1}
.btn{display:inline-flex;align-items:center;justify-content:center;width:180px;height:56px;background:var(--blue);color:#fff;font-size:18px;text-decoration:none}

/* top bar */
.topbar{position:absolute;left:0;width:1200px;top:0;height:47px;background:var(--topbar)}
.social{display:flex;gap:12px;align-items:center}
.social span{width:16px;height:16px;border-radius:50%;background:#fff;display:block}
.topbar .social{position:absolute;left:76px;top:15px}
.contact-line{position:absolute;right:72px;top:0;height:47px;display:flex;align-items:center;gap:28px;color:#fff;font-size:15px}
.contact-line span{display:flex;align-items:center;gap:14px}

/* header */
.site-header{top:47px;height:89px;background:#fff}
.brand{position:absolute;left:74px;top:13px;display:flex;align-items:center;gap:16px}
.brand-square{width:62px;height:62px;background:var(--blue)}
.brand-name{font-weight:900;font-size:23px;line-height:1.15;color:var(--blue);text-transform:uppercase}
.nav{position:absolute;right:74px;top:0;height:89px;display:flex;align-items:center;gap:36px}
.nav a{font-size:13.5px;font-weight:700;color:#222;text-decoration:none;text-transform:uppercase}
.nav a.active{color:var(--blue-link)}

/* hero */
.hero{top:136px;height:589px;background:linear-gradient(160deg,#8fa6bd 0%,#4d6782 35%,#243d57 65%,#1b2c40 100%)}
.hero-text{position:absolute;top:228px;width:100%;text-align:center;color:#fff}
.hero-text .kicker{font-size:46px;font-weight:700;line-height:1}
.hero-text .name{font-size:72px;font-weight:400;line-height:1.1;margin-top:6px}
.hero-arrow{position:absolute;top:271px}

/* about */
.about{top:725px;height:431px;text-align:center}
.about .title{margin-top:57px}
.about p{width:1040px;margin:26px auto 0;text-align:center;font-size:14.5px;line-height:26px}
.about .btn{margin-top:38px}

/* services */
.services{top:1156px;height:415px;background:var(--panel)}
.svc-card{position:absolute;top:60px;width:242px;height:289px;background:#fff;box-shadow:0 1px 5px rgba(0,0,0,.22);text-align:center;padding:34px 20px 0}
.svc-card h3{font-size:19.5px;font-weight:700;color:var(--blue);margin-top:18px;letter-spacing:.3px}
.svc-card p{font-size:14.5px;line-height:23px;margin-top:8px}
.svc-intro{position:absolute;left:613px;top:58px;width:495px}
.svc-intro .title{text-align:left}
.svc-intro p{font-size:14.5px;line-height:26px;margin-top:14px}
.svc-intro .btn{margin-top:25px}

/* gallery */
.gallery{top:1571px;height:554px}
.gallery .title{margin-top:40px}
.grid{position:absolute;left:74px;top:129px;width:1052px;display:grid;grid-template-columns:260px 248px 248px 260px;grid-template-rows:170px 170px;gap:12px}
.ph{display:block}

/* blog */
.blog{top:2125px;height:543px;background:var(--panel)}
.blog .title{margin-top:44px}
.post{position:absolute;top:131px;width:331px;text-align:center}
.post .ph{height:208px}
.post h3{font-size:24px;font-weight:400;color:var(--blue-link);line-height:30px;margin-top:18px;padding:0 22px}
.post p{font-size:14.5px;line-height:23px;margin-top:6px;padding:0 14px}

/* reviews */
.reviews{top:2668px;height:427px}
.reviews .title{margin-top:40px}
.review{position:absolute;top:140px;width:331px;text-align:center}
.review p{font-style:italic;font-size:13.5px;line-height:23px;margin-top:16px;padding:0 8px}
.review .who{font-style:normal;font-weight:700;color:var(--blue-link);font-size:13.5px;margin-top:12px}
.dots{position:absolute;top:354px;left:0;width:100%;display:flex;justify-content:center;gap:10px}
.dots span{width:14px;height:14px;border-radius:50%;background:#333}
.dots span.on{background:var(--blue)}

/* footer */
.site-footer{top:3095px;height:269px;background:var(--footer);color:var(--footer-text)}
.foot-brand{position:absolute;left:74px;top:80px;display:flex;align-items:center;gap:12px}
.foot-brand .sq{width:40px;height:40px;background:#8d8d8d}
.foot-brand .nm{color:#d8d8d8;font-weight:700;font-size:15px}
.copy{position:absolute;left:74px;top:172px;font-size:11px;line-height:18px;color:#ddd}
.fcol{position:absolute;top:62px}
.fcol h4{color:#fff;font-size:16px;font-weight:700;text-transform:uppercase;margin-bottom:10px}
.fcol a,.fcol div.l{display:block;color:var(--footer-text);font-size:14.5px;line-height:30px;text-decoration:none;white-space:nowrap}
.fcol .hl{color:var(--blue-link)}
.fcol div.l.ic{display:flex;align-items:center;gap:18px}
.site-footer .social{gap:16px;margin-top:6px}
.site-footer .social span{width:18px;height:18px}
</style>
</head>
<body>

<div class="topbar">
  <div class="social"><span></span><span></span><span></span><span></span><span></span></div>
  <div class="contact-line">
    <span><svg width="14" height="14" viewBox="0 0 24 24"><path fill="#fff" d="M6.6 10.8a15.1 15.1 0 0 0 6.6 6.6l2.2-2.2c.3-.3.7-.4 1-.2 1.1.4 2.3.6 3.6.6.6 0 1 .4 1 1V20c0 .6-.4 1-1 1A17 17 0 0 1 3 4c0-.6.4-1 1-1h3.5c.6 0 1 .4 1 1 0 1.3.2 2.5.6 3.6.1.3 0 .7-.2 1z"/></svg>1-800-555-0148</span>
    <span><svg width="16" height="13" viewBox="0 0 24 18"><path fill="#fff" d="M0 0h24v3L12 10 0 3zM0 5l12 7 12-7v13H0z"/></svg>hello@hwnstructures.co.uk</span>
  </div>
</div>

<header class="site-header">
  <div class="brand"><div class="brand-square"></div><div class="brand-name">HWN<br>Structures Ltd</div></div>
  <nav class="nav">
    <a class="active" href="#">Home</a><a href="#">About Us</a><a href="#">Services</a><a href="#">Gallery</a><a href="#">Blog</a><a href="#">Testimonials</a><a href="#">Contact Us</a>
  </nav>
</header>

<section class="hero" role="img" aria-label="Photo of workers abseiling down a glass office tower">
  <svg class="hero-arrow" style="left:60px" width="24" height="44" viewBox="0 0 24 44"><path d="M22 2 2 22l20 20" fill="none" stroke="#fff" stroke-width="2.5"/></svg>
  <svg class="hero-arrow" style="right:60px" width="24" height="44" viewBox="0 0 24 44"><path d="M2 2l20 20L2 42" fill="none" stroke="#fff" stroke-width="2.5"/></svg>
  <div class="hero-text"><div class="kicker">WELCOME TO</div><div class="name">HWN STRUCTURES LTD</div></div>
</section>

<section class="about">
  <h2 class="title">About<br>HWN Structures Ltd</h2>
  <p>Aliquam molestie, mi et imperdiet euismod, dui purus auctor tellus, et interdum lacus lectus et ante. Sed accumsan sollicitudin sapien, sit amet adipiscing turpis gravida ac.&nbsp; In congue, neque ac lobortis volutpat, libero mauris varius mi, vitae suscipit ipsum ligula vitae risus. Duis aliquam nibh a dui iaculis viverra id a velit. Vivamus egestas risus in magna varius commodo. Sed semper viverra egestas.</p>
  <a class="btn" href="#">Read More</a>
</section>

<section class="services">
  <div class="svc-card" style="left:74px">
    <svg width="48" height="56" viewBox="0 0 48 56"><rect x="4" y="2" width="40" height="52" fill="none" stroke="#333" stroke-width="4"/><g fill="#333"><rect x="13" y="10" width="7" height="7"/><rect x="28" y="10" width="7" height="7"/><rect x="13" y="22" width="7" height="7"/><rect x="28" y="22" width="7" height="7"/><rect x="13" y="34" width="7" height="7"/><rect x="28" y="34" width="7" height="7"/><rect x="20" y="44" width="8" height="10"/></g></svg>
    <h3>BUILDING</h3>
    <p>Aliquam molestie, mi et imperdiet euismod, dui purus auctor tellus, et&nbsp; interdum lacus lectus et ante.</p>
  </div>
  <div class="svc-card" style="left:344px">
    <svg width="58" height="58" viewBox="0 0 58 58"><path fill="#333" d="M53 12 44 21l-8-2-2-8 9-9C36 0 28 4 27 12c0 3 .5 5 1.5 7L4 43.5a6 6 0 0 0 8.5 8.5L37 27.5c2 1 4 1.5 7 1.5 8-1 12-9 9-17z"/></svg>
    <h3>MAINTENANCE</h3>
    <p>Aliquam molestie, mi et imperdiet euismod, dui purus auctor tellus, et&nbsp; interdum lacus lectus et ante.</p>
  </div>
  <div class="svc-intro">
    <h2 class="title">Our Services</h2>
    <p>Aliquam molestie, mi et imperdiet euismod, dui purus auctor tellus, et interdum lacus lectus et ante. Sed accumsan sollicitudin sapien, sit amet adipiscing turpis gravida ac.&nbsp; In congue, neque ac lobortis volutpat, libero mauris varius mi, vitae suscipit ipsum ligula vitae risusaliquam nibh a dui iaculis viverra id a velit.</p>
    <a class="btn" href="#">Read More</a>
  </div>
</section>

<section class="gallery">
  <h2 class="title">Gallery</h2>
  <div class="grid">
    <div class="ph" role="img" aria-label="Builder fitting a shopfront beside a brick wall" style="background:linear-gradient(135deg,#6b5a4c,#3b3430)"></div>
    <div class="ph" role="img" aria-label="Inspector with clipboard in a finished interior" style="background:linear-gradient(135deg,#e6e2dc,#b7a48e)"></div>
    <div class="ph" role="img" aria-label="Engineers reviewing plans outside a new apartment block" style="grid-row:span 2;background:linear-gradient(180deg,#9eb1c8,#7c7f85 50%,#4b4c50)"></div>
    <div class="ph" role="img" aria-label="Workers abseiling on a grey facade" style="background:linear-gradient(135deg,#8a8c91,#5f6167)"></div>
    <div class="ph" role="img" aria-label="Electrician working on wall wiring" style="background:linear-gradient(135deg,#8e8f8f,#4b586a)"></div>
    <div class="ph" role="img" aria-label="Steel erectors on a structure at sunset" style="background:linear-gradient(135deg,#d98a55,#394560)"></div>
    <div class="ph" role="img" aria-label="Worker pressure washing a metal roof" style="background:linear-gradient(135deg,#5d6a74,#2f3a44)"></div>
  </div>
</section>

<section class="blog">
  <h2 class="title">Blog Posts</h2>
  <article class="post" style="left:74px">
    <div class="ph" role="img" aria-label="Site managers in hard hats inspecting a room" style="background:linear-gradient(135deg,#c9c6c1,#8e8a84)"></div>
    <h3>Neque porro quisquam est qui dolorem ipsum</h3>
    <p>Aliquam molestie, mi et imperdiet euismod, dui purus auctor tellus, et&nbsp; interdum lacus lectus et ante.</p>
  </article>
  <article class="post" style="left:435px">
    <div class="ph" role="img" aria-label="Worker carrying a ladder on a city building site" style="background:linear-gradient(135deg,#a9b0b6,#5d6467)"></div>
    <h3>Neque porro quisquam est qui dolorem ipsum</h3>
    <p>Aliquam molestie, mi et imperdiet euismod, dui purus auctor tellus, et&nbsp; interdum lacus lectus et ante.</p>
  </article>
  <article class="post" style="left:796px">
    <div class="ph" role="img" aria-label="Tall buildings seen from street level at dusk" style="background:linear-gradient(135deg,#2c4f78,#8b7156 60%,#cfd7e2)"></div>
    <h3>Neque porro quisquam est qui dolorem ipsum</h3>
    <p>Aliquam molestie, mi et imperdiet euismod, dui purus auctor tellus, et&nbsp; interdum lacus lectus et ante.</p>
  </article>
</section>

<section class="reviews">
  <h2 class="title">Customer Reviews</h2>
  <div class="review" style="left:74px">
    <svg width="36" height="28" viewBox="0 0 36 28"><path fill="#0b3d9c" d="M0 0h15v15c0 7-4 12-11 13v-5c3-1 5-3 5-7H0zM21 0h15v15c0 7-4 12-11 13v-5c3-1 5-3 5-7h-9z"/></svg>
    <p>Sed accumsan sollicitudin sapien, sit amet adipiscing turpis gravida ac.&nbsp; In congue, neque ac lobortis volutpat, libero mauris varius mi..</p>
    <p class="who">-Name Heading</p>
  </div>
  <div class="review" style="left:435px">
    <svg width="36" height="28" viewBox="0 0 36 28"><path fill="#0b3d9c" d="M0 0h15v15c0 7-4 12-11 13v-5c3-1 5-3 5-7H0zM21 0h15v15c0 7-4 12-11 13v-5c3-1 5-3 5-7h-9z"/></svg>
    <p>Sed accumsan sollicitudin sapien, sit amet adipiscing turpis gravida ac.&nbsp; In congue, neque ac lobortis volutpat, libero mauris varius mi..</p>
    <p class="who">-Name Heading</p>
  </div>
  <div class="review" style="left:796px">
    <svg width="36" height="28" viewBox="0 0 36 28"><path fill="#0b3d9c" d="M0 0h15v15c0 7-4 12-11 13v-5c3-1 5-3 5-7H0zM21 0h15v15c0 7-4 12-11 13v-5c3-1 5-3 5-7h-9z"/></svg>
    <p>Sed accumsan sollicitudin sapien, sit amet adipiscing turpis gravida ac.&nbsp; In congue, neque ac lobortis volutpat, libero mauris varius mi..</p>
    <p class="who">-Name Heading</p>
  </div>
  <div class="dots"><span class="on"></span><span></span><span></span></div>
</section>

<footer class="site-footer">
  <div class="foot-brand"><div class="sq"></div><div class="nm">HWN Structures Ltd</div></div>
  <div class="copy">Copyright © 2021. HWN Structures Ltd.<br>All Right Reserved</div>
  <div class="fcol" style="left:341px">
    <h4>Site Map</h4>
    <a href="#">Home</a><a href="#">About Us</a><a href="#">Services</a><a href="#">Gallery</a>
  </div>
  <div class="fcol" style="left:474px;top:91px">
    <a href="#">Blog</a><a href="#">Testimonials</a><a href="#">Contact Us</a>
  </div>
  <div class="fcol" style="left:622px">
    <h4>Contact Info</h4>
    <div class="l hl">HWN Structures Ltd</div>
    <div class="l" style="line-height:22px;margin-top:4px">14 Kelvin Quay Road,<br>Glasgow, G3 8QT</div>
    <div class="l ic" style="margin-top:2px"><svg width="14" height="14" viewBox="0 0 24 24"><path fill="#b9b9b9" d="M6.6 10.8a15.1 15.1 0 0 0 6.6 6.6l2.2-2.2c.3-.3.7-.4 1-.2 1.1.4 2.3.6 3.6.6.6 0 1 .4 1 1V20c0 .6-.4 1-1 1A17 17 0 0 1 3 4c0-.6.4-1 1-1h3.5c.6 0 1 .4 1 1 0 1.3.2 2.5.6 3.6.1.3 0 .7-.2 1z"/></svg>1-800-555-0148</div>
    <div class="l ic"><svg width="15" height="12" viewBox="0 0 24 18"><path fill="#b9b9b9" d="M0 0h24v3L12 10 0 3zM0 5l12 7 12-7v13H0z"/></svg>hello@hwnstructures.co.uk</div>
  </div>
  <div class="fcol" style="left:885px">
    <h4>Follow Us</h4>
    <div class="social"><span></span><span></span><span></span><span></span><span></span></div>
  </div>
</footer>

</body>
</html>
```